Professional PowerPoint Template for Data Reports, Presentations

We are a small leadership coaching/consulting firm and would like to update our PowerPoint template that we use with our clients, who are typically mid-senior level company professionals. I've attached a sample Powerpoint as well as our branding guide. The cover page is what needs the most work - just doesn't look current/professional enough. We do want to keep the pages after that clean, with come color but enough space for text and graphics.
Target Market(s)
Senior mgmt and HR executives in small-mid sized companies
Font styles to use
Sans Serif
Requirements
Must have
- Professional
- Clean
- Tied to company color scheme/logo
Nice to have
- Our title pages don't usually have many words on them; we'd like a design that has a lot of color - probably still using mainly our blue but accented with other colors.
- Need simple but smart looking pages after cover with lot of space; mostly we have text on the slides. Currently this is often in bullet point style, but we could probably upgrade the options there.
Should not have
- Anything that looks like a marketing style, as we typically use these with our current clients to share results of data collected, project plans, etc.

```html
<!DOCTYPE html>
<html lang="en">
<head>
<meta charset="utf-8">
<title>Meridian Presentation Template</title>
<link href="https://fonts.googleapis.com/css2?family=Montserrat:wght@400;500&display=swap" rel="stylesheet">
<style>
  :root {
    --brand-blue: #14558a;
    --accent-orange: #ee8454;
    --accent-teal: #76b6aa;
    --accent-sky: #41a9f4;
    --panel-gray: #dcdcdc;
    --rule-gray: #c4c4c4;
    --body-top: #e2e2e2;
    --body-mid: #ffffff;
    --body-bottom: #d9d9d9;
    --ink-light: #ffffff;
    --page-bg: #ffffff;
  }
  html, body {
    margin: 0;
    padding: 0;
    width: 1200px;
    height: 1000px;
    overflow: hidden;
    background: var(--page-bg);
    font-family: "Montserrat", sans-serif;
  }
  .template-sheet {
    position: relative;
    width: 1200px;
    height: 1000px;
  }
  .slide {
    position: absolute;
    width: 510px;
    height: 425px;
    filter: drop-shadow(8px 10px 9px rgba(0, 0, 0, 0.35));
  }
  .slide svg { display: block; width: 510px; height: 425px; }
  .slide--cover { left: 48px; top: 50px; }
  .slide--agenda { left: 620px; top: 50px; }
  .slide--content { left: 48px; top: 522px; }
  .slide--content-alt { left: 620px; top: 522px; }
  .brand-band { fill: var(--brand-blue); }
  .brand-rule { fill: var(--rule-gray); }
  .bar-orange { fill: var(--accent-orange); }
  .bar-teal { fill: var(--accent-teal); }
  .bar-sky { fill: var(--accent-sky); }
  .bar-shadow { fill: var(--rule-gray); }
  .title-panel { fill: var(--panel-gray); }
  .wordmark {
    fill: var(--ink-light);
    font-family: "Montserrat", sans-serif;
    font-weight: 500;
  }
  .wordmark-dot { fill: var(--ink-light); }
  .footer-url {
    fill: var(--ink-light);
    font-family: "Montserrat", sans-serif;
    font-weight: 400;
  }
</style>
</head>
<body>
<main class="template-sheet">

  <svg width="0" height="0" style="position:absolute">
    <defs>
      <linearGradient id="slide-body" x1="0" y1="0" x2="0" y2="1">
        <stop offset="0" stop-color="var(--body-top)"/>
        <stop offset="0.28" stop-color="var(--body-mid)"/>
        <stop offset="0.78" stop-color="var(--body-mid)"/>
        <stop offset="1" stop-color="var(--body-bottom)"/>
      </linearGradient>
      <linearGradient id="panel-fade" x1="0" y1="0" x2="0" y2="1">
        <stop offset="0" stop-color="#e4e4e4"/>
        <stop offset="1" stop-color="#d6d6d6"/>
      </linearGradient>
    </defs>
  </svg>

  <!-- Cover slide -->
  <section class="slide slide--cover" aria-label="Cover slide">
    <svg viewBox="0 0 510 425">
      <rect width="510" height="425" fill="url(#slide-body)"/>
      <polygon class="brand-rule" points="0,0 510,0 510,72 249,72 193,129 0,129"/>
      <polygon class="brand-band" points="0,0 510,0 510,68 245,68 189,125 0,125"/>
      <circle class="wordmark-dot" cx="40" cy="62" r="13"/>
      <text class="wordmark" x="66" y="71" font-size="25" letter-spacing="2">MERIDIAN</text>
      <polygon class="bar-shadow" points="270,137 510,137 510,180 228,180"/>
      <polygon class="bar-orange" points="270,133 510,133 510,176 228,176"/>
      <polygon class="title-panel" fill="url(#panel-fade)" points="232,180 510,180 510,353 277,353 232,308"/>
      <rect class="brand-rule" y="394" width="510" height="4"/>
      <rect class="brand-band" y="398" width="510" height="27"/>
      <text class="footer-url" x="255" y="415" font-size="9" text-anchor="middle">www.meridiangroup.com</text>
    </svg>
  </section>

  <!-- Agenda / section slide -->
  <section class="slide slide--agenda" aria-label="Section slide">
    <svg viewBox="0 0 510 425">
      <rect width="510" height="425" fill="url(#slide-body)"/>
      <polygon class="brand-rule" points="0,0 510,0 510,72 249,72 193,129 0,129"/>
      <polygon class="brand-band" points="0,0 510,0 510,68 245,68 189,125 0,125"/>
      <circle class="wordmark-dot" cx="40" cy="62" r="13"/>
      <text class="wordmark" x="66" y="71" font-size="25" letter-spacing="2">MERIDIAN</text>
      <polygon class="bar-shadow" points="270,137 510,137 510,180 228,180"/>
      <polygon class="bar-orange" points="270,133 510,133 510,176 228,176"/>
      <polygon class="bar-shadow" points="298,229 510,229 510,267 258,267"/>
      <polygon class="bar-teal" points="298,225 510,225 510,263 258,263"/>
      <polygon class="bar-shadow" points="312,317 510,317 510,354 273,354"/>
      <polygon class="bar-sky" points="312,313 510,313 510,350 273,350"/>
      <rect class="brand-rule" y="394" width="510" height="4"/>
      <rect class="brand-band" y="398" width="510" height="27"/>
      <text class="footer-url" x="255" y="415" font-size="9" text-anchor="middle">www.meridiangroup.com</text>
    </svg>
  </section>

  <!-- Content slide -->
  <section class="slide slide--content" aria-label="Content slide">
    <svg viewBox="0 0 510 425">
      <rect width="510" height="425" fill="url(#slide-body)"/>
      <polygon class="brand-rule" points="0,0 510,0 510,19 156,19 128,42 0,42"/>
      <polygon class="brand-band" points="0,0 510,0 510,15 152,15 124,38 0,38"/>
      <circle class="wordmark-dot" cx="32" cy="19" r="6"/>
      <text class="wordmark" x="44" y="23.5" font-size="12" letter-spacing="1">MERIDIAN</text>
      <rect class="brand-rule" y="407" width="510" height="3"/>
      <rect class="brand-band" y="410" width="510" height="15"/>
      <text class="footer-url" x="255" y="420" font-size="7" text-anchor="middle">www.meridiangroup.com</text>
    </svg>
  </section>

  <!-- Content slide, alternate -->
  <section class="slide slide--content-alt" aria-label="Content slide alternate">
    <svg viewBox="0 0 510 425">
      <rect width="510" height="425" fill="url(#slide-body)"/>
      <polygon class="brand-rule" points="0,0 510,0 510,19 156,19 128,42 0,42"/>
      <polygon class="brand-band" points="0,0 510,0 510,15 152,15 124,38 0,38"/>
      <circle class="wordmark-dot" cx="32" cy="19" r="6"/>
      <text class="wordmark" x="44" y="23.5" font-size="12" letter-spacing="1">MERIDIAN</text>
      <rect class="brand-rule" y="407" width="510" height="3"/>
      <rect class="brand-band" y="410" width="510" height="15"/>
      <text class="footer-url" x="255" y="420" font-size="7" text-anchor="middle">www.meridiangroup.com</text>
    </svg>
  </section>

</main>
</body>
</html>
```